Historic Church website

We want our church website to feel warm, historic, and clean, modern, and easy to navigate. Dont use the anchor

Current website: https://www.meadowlarkfellowship.org/

Requirements
Should not have
• I would like to use the logo without the anchor

```html
<!DOCTYPE html>
<html lang="en">
<head>
<meta charset="utf-8">
<title>Meadowlark Fellowship</title>
<link href="https://fonts.googleapis.com/css2?family=Oranienbaum&family=Libre+Baskerville:wght@400;700&display=swap" rel="stylesheet">
<style>
:root{
  --gold:#c9a23c;
  --gold-deep:#b48a2a;
  --brown:#1d1109;
  --brown-mid:#2b1a0e;
  --blue:#12305c;
  --blue-deep:#0d2447;
  --button:#4a2414;
  --cream:#f3e6c4;
  --ink:#2a1a0c;
  --accent:#e0b24a;
  --link:#3f8fe0;
}
*{box-sizing:border-box;margin:0;padding:0}
html,body{width:1200px;height:4751px;overflow:hidden;background:#f2f2f2}
body{font-family:"Libre Baskerville",serif;color:var(--cream);position:relative}
.page{position:relative;width:1200px;height:4751px}
section,header,footer{position:absolute;left:0;width:1200px}
.abs{position:absolute}
.display{font-family:"Oranienbaum",serif;text-transform:uppercase;letter-spacing:.5px;font-weight:400;transform:scaleX(.84);transform-origin:center}
.display.left{transform-origin:left center}
.btn{position:absolute;background:var(--button);color:var(--cream);font-size:13px;letter-spacing:1px;text-transform:uppercase;border-radius:20px;padding:9px 22px;text-align:center;white-space:nowrap}
.band-box{position:absolute;left:309px;width:579px;border:2px solid var(--cream);color:var(--cream);text-align:center;font-size:15px;line-height:1.6;letter-spacing:1px;text-transform:uppercase;display:flex;align-items:center;justify-content:center}

/* brand */
.brand{position:absolute;display:flex;align-items:center;gap:10px}
.brand-dot{width:40px;height:40px;border:3px solid var(--cream);border-radius:50%;flex:none}
.brand-name{font-size:12px;line-height:1.35;letter-spacing:2px;text-transform:uppercase;color:var(--cream)}

/* hero */
.hero{top:0;height:583px;background:linear-gradient(180deg,#2a1a10 0%,#3a2414 45%,#1a0f08 100%)}
.hero .brand{left:93px;top:22px}
.nav{position:absolute;left:412px;top:36px;display:flex;gap:38px;font-size:10px;letter-spacing:1px;text-transform:uppercase}
.nav a{color:var(--cream);text-decoration:none}
.nav a.active{color:var(--link);text-decoration:underline}
.hero h1{position:absolute;left:0;width:1200px;top:210px;text-align:center;font-size:60px;line-height:66px;color:#fff}

/* quote */
.quote{top:583px;height:245px;background:var(--blue)}

/* about team */
.about{top:828px;height:589px;background:var(--gold)}
.about h2{position:absolute;left:141px;top:100px;font-size:46px;line-height:52px;color:var(--ink)}
.tile{position:absolute;width:212px;height:194px;border:2px solid var(--button);background:linear-gradient(160deg,#5a4330,#2a1a10);display:flex;align-items:flex-end;justify-content:center;padding-bottom:14px;font-size:12px;letter-spacing:1px;text-transform:uppercase;text-align:center}
.tile.add{background:var(--blue);flex-direction:column;align-items:center;justify-content:center;gap:18px;padding:30px 0 0}
.plus{width:44px;height:44px;border-radius:50%;background:#fff;color:var(--blue);font-size:34px;line-height:44px;text-align:center}

/* newsletter */
.newsletter{top:1417px;height:498px;background:var(--brown)}
.news-art{position:absolute;left:320px;top:95px;width:255px;height:250px;border-radius:50%;background:radial-gradient(circle,#3a2512,#241509)}
.newsletter .kicker{position:absolute;left:548px;top:118px;font-size:28px;color:var(--cream)}
.newsletter h3{position:absolute;left:548px;top:155px;font-size:50px;color:#fff}
.field{position:absolute;height:32px;border:1px solid #4a3422;border-radius:5px;background:#24160c;font-size:11px;color:#8a7a68;padding:9px 0 0 34px}

/* intro */
.intro{top:1915px;height:561px;background:var(--gold)}
.photo-stack{position:absolute;left:178px;top:118px;width:325px;height:330px;background:linear-gradient(150deg,#6b4a2e,#2c1a0e);border:8px solid #fff;transform:rotate(-3deg)}
.intro .copy{position:absolute;left:612px;top:140px;width:430px;color:var(--ink);font-size:10px;line-height:1.45}
.intro .copy h4{font-size:12px;line-height:1.4;text-transform:uppercase;margin-bottom:14px}
.intro .copy p{margin-bottom:12px}

/* sermon */
.sermon{top:2476px;height:229px;background:var(--blue)}

/* visit */
.visit{top:2705px;height:481px;background:var(--brown)}
.visit h2{position:absolute;top:85px;width:1200px;text-align:center;font-size:50px;color:#fff}
.visit .sub{position:absolute;top:150px;width:1200px;text-align:center;font-size:14px;letter-spacing:1px;color:var(--accent);text-transform:uppercase}
.svc{position:absolute;top:198px;width:212px;height:194px;border:2px solid #5b3a14;background:#2a190c;text-align:center;font-size:15px;line-height:1.35;padding-top:100px}
.svc svg{position:absolute;left:86px;top:30px}
.svc .time{display:block;color:var(--accent);font-size:17px;margin-top:4px}

/* events */
.events{top:3186px;height:698px;background:var(--gold)}
.events h2{position:absolute;top:82px;width:1200px;text-align:center;font-size:50px;color:var(--ink)}
.card{position:absolute;width:385px;height:256px;border:2px solid #3a1f10;background:var(--button)}
.card .img{height:183px}
.evt{display:flex;align-items:center;gap:14px;padding:0 16px;font-size:14px}
.evt small{display:block;font-size:11px;margin-top:3px}
.ico{width:34px;height:34px;border:2px solid #b98a60;border-radius:4px;flex:none}
.mini{position:absolute;top:434px;width:276px;height:88px;background:var(--button);border:2px solid #3a1f10;overflow:hidden}
.mini .evt{height:100%}
.arrow{position:absolute;left:1083px;top:463px;width:28px;height:28px;border-radius:50%;background:#1d1109;color:#fff;font-size:14px;text-align:center;line-height:28px}

/* testimonials */
.testimonials{top:3884px;height:447px;background:var(--blue)}
.testimonials h2{position:absolute;top:62px;width:1200px;text-align:center;font-size:50px;color:#fff}
.qcircle{position:absolute;left:363px;top:153px;width:96px;height:96px;border-radius:50%;background:#fff;border:4px solid var(--link)}
.testimonials .text{position:absolute;left:500px;top:138px;width:580px;font-size:13px;line-height:1.5}
.person{position:absolute;left:500px;top:262px;display:flex;align-items:center;gap:14px;font-size:11px}
.avatar{width:40px;height:40px;border-radius:50%;background:#b89878;border:2px solid #fff}
.person b{color:var(--link);font-weight:400;display:block}
.dots{position:absolute;left:822px;top:274px;display:flex;gap:7px}
.dots i{width:9px;height:9px;border-radius:50%;border:1px solid #fff;display:block}
.dots i.on{background:#fff}

/* footer */
.site-footer{top:4331px;height:420px;background:var(--brown);font-size:10.5px;line-height:1.9}
.site-footer .brand{left:420px;top:55px}
.site-footer .brand-dot{width:50px;height:50px}
.site-footer .brand-name{font-size:15px}
.col-title{color:var(--link);font-size:11px;letter-spacing:1px;text-transform:uppercase;margin-bottom:6px}
.contact{position:absolute;left:230px;top:148px}
.contact div{display:flex;gap:8px;align-items:flex-start}
.links{position:absolute;left:435px;top:148px}
.links .grid{display:grid;grid-template-columns:118px 120px}
.links .grid a{color:var(--cream);text-decoration:none;white-space:nowrap}
.links .grid a.active{color:var(--link);text-decoration:underline}
.social{display:flex;gap:10px;margin-top:10px}
.social i{width:22px;height:22px;border:1px solid var(--cream);border-radius:50%;display:block}
.map{position:absolute;left:725px;top:72px;width:316px;height:284px;border:3px solid var(--link);background:linear-gradient(135deg,#e8e6e0,#d4dde6)}
.copyright{position:absolute;top:342px;left:312px;font-size:10px}
.copyright span{color:var(--link)}
</style>
</head>
<body>
<div class="page">

<header class="hero">
  <div role="img" aria-label="Candlelit historic church sanctuary with stained glass windows" class="abs" style="inset:0;background:radial-gradient(ellipse at 50% 30%,rgba(90,70,60,.55),rgba(20,12,6,0) 65%)"></div>
  <div class="brand"><span class="brand-dot"></span><span class="brand-name">Meadowlark<br>Fellowship</span></div>
  <nav class="nav"><a class="active" href="#">Home</a><a href="#">About MFC</a><a href="#">Ministries</a><a href="#">Bible Studies</a><a href="#">Sermon Library</a></nav>
  <div class="btn" style="left:1007px;top:24px">Donate</div>
  <h1 class="display">Ancient Church. Ancient<br>Faith. Eternal Truth.</h1>
  <div class="btn" style="left:502px;top:354px;width:196px">Join Our Community</div>
</header>

<section class="quote">
  <div class="band-box" style="top:65px;height:103px">We have this hope as an anchor for the<br>soul, firm and secure. - Heb 6:19</div>
</section>

<section class="about">
  <h2 class="display left">About<br>MFC</h2>
  <div class="tile" role="img" aria-label="Senior pastor in prayer" style="left:376px;top:82px">Senior Pastor</div>
  <div class="tile" role="img" aria-label="Elder speaking at a lectern" style="left:611px;top:82px">Elders &amp; Deacons</div>
  <div class="tile" role="img" aria-label="Children reading in church" style="left:845px;top:82px">Children's Ministry</div>
  <div class="tile" role="img" aria-label="Men studying together" style="left:141px;top:298px">Men's Ministry</div>
  <div class="tile" role="img" aria-label="Women in worship" style="left:376px;top:298px">Women's Ministry</div>
  <div class="tile add" style="left:611px;top:298px"><span class="plus">+</span><span>Office<br>Administrator</span></div>
  <div class="tile" role="img" aria-label="Church treasurer" style="left:845px;top:298px">Treasurer</div>
</section>

<section class="newsletter">
  <div class="news-art" role="img" aria-label="Gold line illustration of a scroll and envelope"></div>
  <div class="kicker display left">Sign up for our</div>
  <h3 class="display left">Weekly Newsletter</h3>
  <div class="field" style="left:548px;top:248px;width:493px">Name</div>
  <div class="field" style="left:548px;top:300px;width:240px">Phone</div>
  <div class="field" style="left:801px;top:300px;width:240px">Email</div>
  <div class="btn" style="left:550px;top:358px">Click to Send</div>
</section>

<section class="intro">
  <div class="photo-stack" role="img" aria-label="Stack of photos of a wood-panelled study with a globe and leather chair"></div>
  <div class="copy">
    <h4>Meadowlark Fellowship is an independent Christian church in the Protestant tradition.</h4>
    <p>Its Central Tenets Are Found In Its Articles Of Faith And Include Belief In: The Deity And Lordship Of Jesus Christ; The Trinity; Jesus' Perfect Life, Atoning Death On The Cross, Bodily Resurrection, And Ascension; Jesus' Literal Return; The Inerrancy Of The Bible In Its Original Manuscripts; And Our Need For Salvation Through Personal Faith In Jesus Christ.</p>
    <p>In Keeping With The Prevailing Perspective Of The Church During The Centuries Immediately Following The Apostles, We Teach Premillennialism. That Is, The Belief That Messiah Will Physically And Literally Return To Earth At Jerusalem Before The Millennial Age Commences. At That Time, He Will Establish A Kingdom Over Which He Will Preside As King. All The Promises Of Israel's Covenants Will Be Literally Fulfilled During This Reign.</p>
    <p>At The End Of One Thousand Years, The Kingdom Will Be Transferred From The Son To The Father (1 Cor 15:24-25) And It Will Merge With The Eternal Kingdom (Rev 20-22).</p>
  </div>
</section>

<section class="sermon">
  <div class="band-box" style="top:61px;height:107px">If you cannot join us in person click here<br>for this week's sermon</div>
</section>

<section class="visit">
  <h2 class="display">Visit Us This Sunday</h2>
  <div class="sub">Flip the boxes for more information</div>
  <div class="svc" style="left:252px"><svg width="40" height="40" viewBox="0 0 40 40" fill="none" stroke="#e0b24a" stroke-width="2"><path d="M20 4v32M8 14h24"/><circle cx="20" cy="28" r="6"/></svg>Morning<br>Worship Service<span class="time">11:00 AM</span></div>
  <div class="svc" style="left:493px"><svg width="40" height="40" viewBox="0 0 40 40" fill="none" stroke="#e0b24a" stroke-width="2"><circle cx="20" cy="20" r="14"/><circle cx="20" cy="20" r="8"/></svg>All Church<br>Lunch<span class="time">12:15 PM</span></div>
  <div class="svc" style="left:736px"><svg width="40" height="40" viewBox="0 0 40 40" fill="none" stroke="#e0b24a" stroke-width="2"><rect x="7" y="6" width="26" height="28" rx="2"/><path d="M20 6v28"/></svg>Afternoon Adult<br>Bible Study<span class="time">12:45 PM</span></div>
</section>

<section class="events">
  <h2 class="display">Upcoming MFC Events</h2>
  <div class="card" style="left:203px;top:154px"><div class="img" role="img" aria-label="Study with a globe and an antique world map" style="background:linear-gradient(135deg,#6a4a30,#3a2414)"></div><div class="evt" style="height:69px"><span class="ico"></span><div>Sunday Service<small>Jan 25 @ 11:00 Am – 12:15 Pm</small></div></div></div>
  <div class="card" style="left:612px;top:154px"><div class="img" role="img" aria-label="Exterior wall of the church building" style="background:linear-gradient(135deg,#d8d2c6,#9c968c)"></div><div class="evt" style="height:69px"><span class="ico"></span><div>Wednesday Night Bible Study<small>Jan 21 @ 7:30 Pm – 8:30 Pm</small></div></div></div>
  <div class="mini" style="left:203px"><div class="evt"><span class="ico"></span><div>Sunday Service<small>Jan 25 @ 11:00 Am – 12:15 Pm</small></div></div></div>
  <div class="mini" style="left:499px"><div class="evt"><span class="ico"></span><div>Wednesday Night<br>Bible Study<small>Jan 25 @ 11:00 Am – 12:15 Pm</small></div></div></div>
  <div class="mini" style="left:798px"><div class="evt"><span class="ico"></span><div>Sunday Service<small>Jan 25 @ 11:00 Am – 12:15 Pm</small></div></div></div>
  <div class="mini" style="left:1096px;width:104px;border-right:0;opacity:.6"><div class="evt"><span class="ico"></span><div>Wed<br>Bibl</div></div></div>
  <div class="arrow">›</div>
  <div class="btn" style="left:546px;top:562px;width:108px">View All</div>
</section>

<section class="testimonials">
  <h2 class="display">Testimonials</h2>
  <div class="qcircle"><svg width="88" height="88" viewBox="0 0 88 88"><path fill="#3f8fe0" d="M26 46h12v14H24V48q0-10 10-14v5q-6 2-8 7zM50 46h12v14H48V48q0-10 10-14v5q-6 2-8 7z"/></svg></div>
  <div class="text">Lorem Ipsum is simply dummy text of the printing and typesetting industry. Lorem Ipsum has been the industry's standard dummy text ever since the 1500s, when an unknown printer took a galley of type and scrambled it to make a type specimen book. It has survived not only five centuries, but also the leap into electronic typesetting, remaining essentially unchanged.</div>
  <div class="person"><span class="avatar" role="img" aria-label="Member portrait"></span><div><b>Elena Marsh</b>Lorem Ipsum</div></div>
  <div class="dots"><i></i><i></i><i class="on"></i><i></i></div>
  <div class="btn" style="left:546px;top:333px;width:108px">View All</div>
</section>

<footer class="site-footer">
  <div class="brand"><span class="brand-dot"></span><span class="brand-name">Meadowlark<br>Fellowship</span></div>
  <div class="contact">
    <div class="col-title">Contact Info</div>
    <div><svg width="11" height="11" viewBox="0 0 12 12"><path fill="#f3e6c4" d="M2 1l3 2-1 2q1 2 3 3l2-1 2 3-2 1Q4 10 1 3z"/></svg>555.014.2290</div>
    <div><svg width="11" height="11" viewBox="0 0 12 12"><rect x="1" y="2.5" width="10" height="7" fill="#f3e6c4"/></svg>info@meadowlarkfellowship.org</div>
    <div><svg width="11" height="13" viewBox="0 0 12 14"><path fill="#f3e6c4" d="M6 0a4.5 4.5 0 0 0-4.5 4.5C1.5 8 6 14 6 14s4.5-6 4.5-9.5A4.5 4.5 0 0 0 6 0z"/></svg><span>2210 Linden Avenue<br>Fairhaven, Oregon 97000</span></div>
    <div class="social"><i></i><i></i><i></i><i></i></div>
  </div>
  <div class="links">
    <div class="col-title">Quick Links</div>
    <div class="grid">
      <a class="active" href="#">Home</a><a href="#">Visiting On A Sunday</a>
      <a href="#">About MFC</a><a href="#">Kids Church</a>
      <a href="#">Ministries</a><a href="#">Event Calendar</a>
      <a href="#">Bible Studies</a><a href="#">Our Ministries</a>
      <a href="#">Sermon Library</a><a href="#">Sermon Library</a>
      <a href="#">Sunday Bible Studies</a><a href="#">Contact Us</a>
    </div>
  </div>
  <div class="map" role="img" aria-label="Street map showing the church location"></div>
  <div class="copyright">© 2026 <span>Harborlight Studio</span>. All Right Reserved</div>
</footer>

</div>
</body>
</html>
```